Mortgage Map Flyer / Email Design

To create a one page document / email that shows a map / road map of the Mortgage Process

Client decides to Purchase a Home
Client find a reputable lenders, typically online or through a trusted friend / resource
Sets an appointment to either meet with that Lender / Loan officer in person, or speaks on the phone
Review credit and borrower documents
Pre Qualification so we stay within the budget of the client or a plan is put in place to help borrower qualify for the purchase they are seeking
Find a trust Realtor to search for homes
Tour homes to find the right fit for the client and their family
Make an offer
Ratify the contract & sign loan disclosures
Go into underwriting
Loan Approval
Sign final loan documents
Fund and move in!

Target Market(s)

Clients looking to purchase a home

Industry/Entity Type

Mortgage

Font styles to use
Sans Serif

Requirements
Must have
• Pictures, road map or map with arrows pointing the way through the process. Want to have something I can print, or embed in an email
Nice to have
• Looking to have similar colors and feel as our branch website, with our loan process videos at www.rlkhome.example
• Our logo and colors would be obviously nice to tie in as well!

```html
<!DOCTYPE html>
<html lang="en">
<head>
<meta charset="utf-8">
<title>Ridgeline Bank – The Mortgage Road Map</title>
<link rel="stylesheet" href="https://fonts.googleapis.com/css2?family=Open+Sans:wght@400;600;700&display=swap">
<style>
  :root {
    --sky-light: #3db0ee;
    --sky-deep: #1a86c8;
    --road: #e4e2df;
    --panel: #e6e4e1;
    --ink: #1d1d1d;
    --white: #ffffff;
    --red: #e2504f;
    --green: #5fae8a;
    --plum: #6a5866;
    --gold: #f4b11d;
    --teal: #137a78;
    --orange: #ee7a4f;
  }
  * { margin: 0; padding: 0; box-sizing: border-box; }
  html, body { width: 1200px; height: 2400px; overflow: hidden; }
  body { font-family: "Open Sans", Arial, sans-serif; }
  .roadmap {
    position: relative;
    width: 1200px;
    height: 2400px;
    overflow: hidden;
    background: linear-gradient(90deg, var(--sky-light) 0%, #2a9fe2 50%, var(--sky-deep) 100%);
  }
  .road-art { position: absolute; inset: 0; }
  .brand {
    position: absolute;
    left: 0; top: 0;
    width: 500px;
    text-align: center;
    padding-top: 52px;
  }
  .brand-square {
    display: block;
    width: 76px; height: 76px;
    margin: 0 auto 28px;
    background: var(--ink);
  }
  .brand-name {
    font-family: "Open Sans", Arial, sans-serif;
    font-weight: 400;
    font-size: 30px;
    letter-spacing: 4px;
    color: var(--ink);
  }
  .step-label {
    position: absolute;
    color: var(--white);
    width: 370px;
  }
  .step-label.right { left: 816px; text-align: left; }
  .step-label.left { right: 784px; text-align: right; }
  .step-title {
    font-weight: 700;
    font-size: 34px;
    line-height: 40px;
  }
  .step-note {
    font-weight: 400;
    font-size: 27px;
    line-height: 30px;
  }
  .num { font-family: "Open Sans", Arial, sans-serif; font-weight: 700; font-size: 44px; }
</style>
</head>
<body>
<main class="roadmap">
  <svg class="road-art" width="1200" height="2400" viewBox="0 0 1200 2400" aria-hidden="true">
    <defs>
      <g id="plus"><path d="M-7 0H7M0 -7V7" stroke="#fff" stroke-width="3.5" stroke-linecap="round"/></g>
    </defs>
    <!-- header panel -->
    <path d="M0 0H660V150Q660 240 570 240H0Z" fill="var(--panel)"/>
    <!-- road -->
    <path fill="none" stroke="var(--road)" stroke-width="52" stroke-linecap="round"
      d="M570 -40 L570 140
         C390 170 446 286 626 316
         C806 346 750 464 570 494
         C390 524 446 642 626 672
         C806 702 750 820 570 850
         C390 880 446 996 626 1026
         C806 1056 750 1170 570 1200
         C390 1230 446 1346 626 1376
         C806 1406 750 1524 570 1554
         C390 1584 446 1702 626 1732
         C806 1762 750 1876 570 1906
         C390 1936 446 2052 626 2082
         C806 2112 750 2228 570 2258
         L570 2440"/>

    <!-- connectors -->
    <g stroke-width="5">
      <line x1="620" y1="140" x2="766" y2="140" stroke="var(--red)"/>
      <line x1="576" y1="316" x2="456" y2="316" stroke="var(--green)"/>
      <line x1="620" y1="494" x2="766" y2="494" stroke="var(--plum)"/>
      <line x1="576" y1="672" x2="456" y2="672" stroke="var(--gold)"/>
      <line x1="620" y1="850" x2="766" y2="850" stroke="var(--teal)"/>
      <line x1="576" y1="1026" x2="456" y2="1026" stroke="var(--orange)"/>
      <line x1="620" y1="1200" x2="766" y2="1200" stroke="var(--red)"/>
      <line x1="576" y1="1376" x2="456" y2="1376" stroke="var(--green)"/>
      <line x1="620" y1="1554" x2="766" y2="1554" stroke="var(--plum)"/>
      <line x1="576" y1="1732" x2="456" y2="1732" stroke="var(--gold)"/>
      <line x1="620" y1="1906" x2="766" y2="1906" stroke="var(--teal)"/>
      <line x1="576" y1="2082" x2="456" y2="2082" stroke="var(--orange)"/>
      <line x1="620" y1="2258" x2="766" y2="2258" stroke="var(--red)"/>
    </g>
    <g>
      <circle cx="766" cy="140" r="15" fill="var(--red)"/><use href="#plus" x="766" y="140"/>
      <circle cx="456" cy="316" r="15" fill="var(--green)"/><use href="#plus" x="456" y="316"/>
      <circle cx="766" cy="494" r="15" fill="var(--plum)"/><use href="#plus" x="766" y="494"/>
      <circle cx="456" cy="672" r="15" fill="var(--gold)"/><use href="#plus" x="456" y="672"/>
      <circle cx="766" cy="850" r="15" fill="var(--teal)"/><use href="#plus" x="766" y="850"/>
      <circle cx="456" cy="1026" r="15" fill="var(--orange)"/><use href="#plus" x="456" y="1026"/>
      <circle cx="766" cy="1200" r="15" fill="var(--red)"/><use href="#plus" x="766" y="1200"/>
      <circle cx="456" cy="1376" r="15" fill="var(--green)"/><use href="#plus" x="456" y="1376"/>
      <circle cx="766" cy="1554" r="15" fill="var(--plum)"/><use href="#plus" x="766" y="1554"/>
      <circle cx="456" cy="1732" r="15" fill="var(--gold)"/><use href="#plus" x="456" y="1732"/>
      <circle cx="766" cy="1906" r="15" fill="var(--teal)"/><use href="#plus" x="766" y="1906"/>
      <circle cx="456" cy="2082" r="15" fill="var(--orange)"/><use href="#plus" x="456" y="2082"/>
      <circle cx="766" cy="2258" r="15" fill="var(--red)"/><use href="#plus" x="766" y="2258"/>
    </g>

    <!-- step markers -->
    <g class="markers">
      <g transform="translate(570 140)"><circle r="64" fill="var(--red)"/><circle r="46" cy="3" fill="rgba(0,0,0,.15)"/><circle r="44" fill="#fff"/><text class="num" text-anchor="middle" dy="16" fill="var(--red)">01</text></g>
      <g transform="translate(626 316)"><circle r="64" fill="var(--green)"/><circle r="46" cy="3" fill="rgba(0,0,0,.15)"/><circle r="44" fill="#fff"/><text class="num" text-anchor="middle" dy="16" fill="var(--green)">02</text></g>
      <g transform="translate(570 494)"><circle r="64" fill="var(--plum)"/><circle r="46" cy="3" fill="rgba(0,0,0,.15)"/><circle r="44" fill="#fff"/><text class="num" text-anchor="middle" dy="16" fill="var(--plum)">03</text></g>
      <g transform="translate(626 672)"><circle r="64" fill="var(--gold)"/><circle r="46" cy="3" fill="rgba(0,0,0,.15)"/><circle r="44" fill="#fff"/><text class="num" text-anchor="middle" dy="16" fill="var(--gold)">04</text></g>
      <g transform="translate(570 850)"><circle r="64" fill="var(--teal)"/><circle r="46" cy="3" fill="rgba(0,0,0,.15)"/><circle r="44" fill="#fff"/><text class="num" text-anchor="middle" dy="16" fill="var(--teal)">05</text></g>
      <g transform="translate(626 1026)"><circle r="64" fill="var(--orange)"/><circle r="46" cy="3" fill="rgba(0,0,0,.15)"/><circle r="44" fill="#fff"/><text class="num" text-anchor="middle" dy="16" fill="var(--orange)">06</text></g>
      <g transform="translate(570 1200)"><circle r="64" fill="var(--red)"/><circle r="46" cy="3" fill="rgba(0,0,0,.15)"/><circle r="44" fill="#fff"/><text class="num" text-anchor="middle" dy="16" fill="var(--red)">07</text></g>
      <g transform="translate(626 1376)"><circle r="64" fill="var(--green)"/><circle r="46" cy="3" fill="rgba(0,0,0,.15)"/><circle r="44" fill="#fff"/><text class="num" text-anchor="middle" dy="16" fill="var(--green)">08</text></g>
      <g transform="translate(570 1554)"><circle r="64" fill="var(--plum)"/><circle r="46" cy="3" fill="rgba(0,0,0,.15)"/><circle r="44" fill="#fff"/><text class="num" text-anchor="middle" dy="16" fill="var(--plum)">09</text></g>
      <g transform="translate(626 1732)"><circle r="64" fill="var(--gold)"/><circle r="46" cy="3" fill="rgba(0,0,0,.15)"/><circle r="44" fill="#fff"/><text class="num" text-anchor="middle" dy="16" fill="var(--gold)">10</text></g>
      <g transform="translate(570 1906)"><circle r="64" fill="var(--teal)"/><circle r="46" cy="3" fill="rgba(0,0,0,.15)"/><circle r="44" fill="#fff"/><text class="num" text-anchor="middle" dy="16" fill="var(--teal)">11</text></g>
      <g transform="translate(626 2082)"><circle r="64" fill="var(--orange)"/><circle r="46" cy="3" fill="rgba(0,0,0,.15)"/><circle r="44" fill="#fff"/><text class="num" text-anchor="middle" dy="16" fill="var(--orange)">12</text></g>
      <g transform="translate(570 2258)"><circle r="64" fill="var(--red)"/><circle r="46" cy="3" fill="rgba(0,0,0,.15)"/><circle r="44" fill="#fff"/><text class="num" text-anchor="middle" dy="16" fill="var(--red)">13</text></g>
    </g>
  </svg>

  <header class="brand">
    <span class="brand-square"></span>
    <span class="brand-name">RIDGELINE BANK</span>
  </header>

  <div class="step-label right" style="top:100px"><p class="step-title">Client decides to<br>Purchase a Home</p></div>
  <div class="step-label left" style="top:276px"><p class="step-title">Client find a<br>reputable lenders</p><p class="step-note">(typically online or<br>through a trusted<br>friend / resource)</p></div>
  <div class="step-label right" style="top:456px"><p class="step-title">Sets an<br>appointment<br>with Loan Officer</p><p class="step-note">(either meet in person<br>or on phone)</p></div>
  <div class="step-label left" style="top:632px"><p class="step-title">Review credit<br>and borrower<br>documents</p></div>
  <div class="step-label right" style="top:828px"><p class="step-title">Pre Qualification</p><p class="step-note">(so we stay within the<br>budget of the client or<br>a plan is put in place to<br>help borrower qualify<br>for the purchase<br>they are seeking)</p></div>
  <div class="step-label left" style="top:986px"><p class="step-title">Find a trust Realtor<br>to search for homes</p></div>
  <div class="step-label right" style="top:1160px"><p class="step-title">Tour homes to<br>find the right fit<br>for the client<br>and their family</p></div>
  <div class="step-label left" style="top:1354px"><p class="step-title">Make an offer</p></div>
  <div class="step-label right" style="top:1514px"><p class="step-title">Ratify the<br>contract &amp; sign<br>loan disclosures</p></div>
  <div class="step-label left" style="top:1692px"><p class="step-title">Go into<br>underwriting</p></div>
  <div class="step-label right" style="top:1884px"><p class="step-title">Loan Approval</p></div>
  <div class="step-label left" style="top:2042px"><p class="step-title">Sign final<br>loan documents</p></div>
  <div class="step-label right" style="top:2236px"><p class="step-title">Fund and move in!</p></div>
</main>
</body>
</html>
```